Professional Lawn Treatment flyer (double sided) needed for established gardening company

We are an established and trusted gardening company in Swindon, UK, and are about to launch a new Lawn Treatment Service. This will be marketed to both existing and new customers and needs to reflect our current professional image. The flyer will need to be double-sided, portrait orientation and correctly sized so to be printed on A5.

If you look on our website www.pelhamgardening.co.uk, you will see our colours are purple and green. We would like you to use these exact shades of purple and green in your design.

As part of the design, we will need you to put together an infographic table to show our packages. I have attached a spreadsheet which explains these packages but I will need you to create a visually appealing table that fits in with the overall design of the flyer. I don't want you to simply cut and paste my basic table into the design.

In terms of what needs to be included, I have tried to be as specific as possible here but please feel free to message me if you need any further information or clarification.

FRONT SIDE:
The title of our service is:
Expert Lawn Treatment Service

Our strapline will need to be included somewhere:
"Lawn care by your local gardening expert"

The front side of the flyer will need to contain our logo - different versions of which can be found within my dropbox folder here...

https://www.filecrate.net/sh/k7bq24nwxe9/QWT8PmRzLxKd3VuYcH0BnJeFa?dl=0

The front side will need to contain a main image (although feel free to add more if you have anything suitable). I have included a picture in the dropbox folder titled "Front side image" which we would like used. I've also included in the folder an adobe image of grass which you may or may not like to use on either front or back.

Somewhere on both the front and back sides, you will need to include our contact details:
01632 960481
www.pelhamgardening.co.uk/lawncare

The front side should show what treatments we currently have available. These are:

- Lawn Fertilising
- Scarification
- Aeration
- Weed Control
- Moss Control
- Hydration Booster
- Kempix
- Turfing & Renovation

"Select a one-off treatment or choose from one of our specially created lawn care packages."

BACK SIDE:
On the back, we will still need our logo and contact details but the image we'd like used should be the one in the dropbox folder titled "Back side image". Again, if you have any other images you feel would also work, then please feel free to add them.

The back side is to contain a bit more information and be a bit 'wordier' and so can you please include the following 2 paragraphs:

"As expert gardeners, we are passionate about horticulture and working to bring out the very best in your garden. When we work in your garden, we look at it and treat it with the same care and attention as if it were our own, before handing it back for you to enjoy. Our passion doesn't end at just trees and shrubs though. Your grass is as much of a living, breathing plant as your shrubs and we therefore utilise our expert horticultural knowledge to ensure your lawn thrives and reaches its fullest potential.

Lawn care isn't just about applying a fertiliser. It's about really understanding your lawn and being able to use extensive knowledge and experience to diagnose and treat issues. It therefore stands to reason that you should employ an expert to bring out the best in your lawn which is why we at Pelham Gardening Services have created a superior lawn care service that will keep your lawn looking lush, green and healthy all year round."

I referred at the very top of this brief to the fact we will need an infographic table created to show the different lawn care packages available. You see from the PDF table I created that we have 3 packages; Standard, Enhanced and Premium. Please create a visually appealing table which sets out the differences between our packages and include it on the back page.

Finally, somewhere we would like reference to the other gardening services we do. It's only to be something small as it isn't the main focus of the flyer but we think it would be good to mention what else we do. To re-iterate, it isnt to be big. I still want the main focus to be lawn care but if you could somehow reference that we also do the following services, that would be good. I will leave it to you to decide where on the flyer it fits in best, be it the front or back:

- Lawn mowing
- Shrub pruning
- Hedge trimming
- Weed killing
- Garden clearance & tidy-up
- Planting & design
- Regular Garden Maintenance
- Turfing
- Fencing
- Gutter clearance

I think thats it. I look forward to your designs!
Ps. Don't forget the dropbox folder:

Target Market(s)

Professional men/women aged 25+
Retired aged 65+

Industry/Entity Type

Home And Garden

Font styles to use
Sans Serif

Colors
6b449b
9bcb3c

Requirements
Must have
• Our company colours; purple and green; as per our website www.pelhamgardening.co.uk. I've selected purple and green on this brief just to highlight the colours needed but please be sure to use the exact shades from our website and NOT the shade of purple and green that were selected on this brief.
• All the wording as explained in the main project brief.
Nice to have
• I want the flyer to be bold, eye-catching and modern.
• We particularly like the font Trebuchet MS for general copy but please feel free to use any other font for bolder, main titles.
Should not have
• We don't want anything gimmicky. No cheesy marketing.
• We only want professional looking designs. With the greatest of respect, if you're just starting out or don't really do design but think you'll use this as practise, please don't waste your or our time. We've previously run contests for other projects where we've had designs submitted that have clearly been done on MS Word and used Clipart and Wordart. That's really not what we are looking for.

```html
<!DOCTYPE html>
<html lang="en">
<head>
<meta charset="utf-8">
<title>Pelham Gardening Services – Expert Lawn Treatment Service flyer</title>
<link rel="stylesheet" href="https://fonts.googleapis.com/css2?family=Source+Sans+3:wght@600;700&family=Open+Sans:wght@400;600;700&display=swap">
<style>
:root{
  --purple:#6b2c84;
  --purple-dark:#52206a;
  --green:#2f6a32;
  --green-deep:#23552a;
  --green-light:#9bcb3c;
  --green-pale:#b5dc7a;
  --paper:#f4f4f4;
  --paper-shade:#d9d9d9;
  --ink:#2b2b2b;
  --stage:#e9e7e3;
  --white:#ffffff;
}
*{box-sizing:border-box;margin:0;padding:0}
html,body{width:1200px;height:1000px;overflow:hidden;background:var(--stage)}
body{position:relative;font-family:"Open Sans",Arial,sans-serif}
.flyer{position:absolute;top:75px;width:548px;height:778px;overflow:hidden;background:var(--paper);box-shadow:0 4px 14px rgba(0,0,0,.25)}
.flyer--front{left:24px}
.flyer--back{left:608px}
.flyer__shapes{position:absolute;inset:0;width:548px;height:778px}
.brand{position:absolute;left:22px;top:40px;display:flex;align-items:center;gap:8px}
.brand__dot{width:16px;height:16px;border-radius:50%;background:var(--green-light)}
.brand__name{font-family:"Source Sans 3",sans-serif;font-weight:700;font-size:17px;line-height:1.05;color:var(--green);width:130px}
.title{position:absolute;right:38px;top:14px;text-align:right;font-family:"Source Sans 3",sans-serif;font-weight:700;font-size:26px;line-height:24px;color:var(--purple)}
.pill{position:absolute;left:50%;transform:translateX(-50%);background:var(--purple);color:var(--white);font-size:15px;font-weight:600;padding:0 8px;line-height:20px;white-space:nowrap}
.checklist{position:absolute;left:20px;right:20px;display:flex;flex-wrap:wrap;justify-content:center;column-gap:16px;list-style:none;color:var(--white);font-size:13.5px}
.checklist li{display:flex;align-items:center;gap:6px;line-height:23px;white-space:nowrap}
.checklist li::before{content:"";width:8px;height:8px;border:1px solid var(--green-pale);background:linear-gradient(45deg,transparent 45%,var(--green-pale) 46%,var(--green-pale) 56%,transparent 57%)}
.divider{position:absolute;left:128px;width:288px;top:525px;height:1px;background:var(--green-pale)}
.divider::after{content:"";position:absolute;left:50%;top:-3px;transform:translateX(-50%);width:54px;height:6px;background:radial-gradient(circle,var(--green-pale) 2.4px,transparent 2.6px) 0 0/7px 6px}
.strap{position:absolute;left:110px;top:661px;width:316px;height:36px;background:var(--green-deep);border:1px solid var(--white);border-radius:3px;color:var(--white);font-size:13.5px;font-weight:600;display:flex;align-items:center;justify-content:center}
.invite{position:absolute;left:0;right:0;top:714px;text-align:center;font-size:10px;font-weight:700;line-height:12px;color:var(--ink)}
.contact{position:absolute;left:0;right:0;top:744px;text-align:center;font-size:13px;font-weight:600;color:var(--ink);display:flex;justify-content:center;align-items:center;gap:5px}
.contact__phone{color:var(--purple);font-family:"Source Sans 3",sans-serif;font-weight:700;font-size:17px}
.contact__icon{width:13px;height:13px}
.copy{position:absolute;color:var(--white);font-size:10px;line-height:13.4px;text-align:justify}
.copy--intro{left:37px;top:412px;width:206px}
.copy--detail{left:37px;top:598px;width:476px}
.packages{position:absolute;left:247px;top:413px;width:261px;height:148px;background:#3d7a3a;border-radius:3px}
.packages__title{height:21px;background:var(--green-pale);border-radius:3px 3px 0 0;text-align:center;font-family:"Source Sans 3",sans-serif;font-weight:700;font-size:14px;line-height:21px;color:var(--green-deep)}
.packages table{width:100%;border-collapse:collapse;color:var(--white);font-size:6.6px;font-weight:700}
.packages th{font-size:5.2px;font-weight:700;height:13px;text-align:center;letter-spacing:.1px}
.packages th:first-child{width:96px}
.packages td{height:13.6px;text-align:center}
.packages td:first-child{text-align:left;padding-left:7px}
.tick{display:inline-block;width:9px;height:9px;border-radius:50%;background:var(--green-pale);position:relative;vertical-align:middle}
.tick::after{content:"";position:absolute;left:2.6px;top:1.4px;width:2.5px;height:4.5px;border:solid var(--white);border-width:0 1.4px 1.4px 0;transform:rotate(45deg)}
</style>
</head>
<body>

<!-- FRONT SIDE -->
<section class="flyer flyer--front">
  <svg class="flyer__shapes" viewBox="0 0 548 778" aria-hidden="false">
    <defs>
      <linearGradient id="paperFront" x1="0" y1="0" x2="0" y2="1"><stop offset="0" stop-color="#ffffff"/><stop offset="1" stop-color="#d6d6d6"/></linearGradient>
      <linearGradient id="lawnFront" x1="0" y1="0" x2="1" y2="1"><stop offset="0" stop-color="#7fae4a"/><stop offset=".45" stop-color="#b9b8a6"/><stop offset="1" stop-color="#3f8a2a"/></linearGradient>
      <linearGradient id="thumb" x1="0" y1="0" x2="0" y2="1"><stop offset="0" stop-color="#8bab5e"/><stop offset="1" stop-color="#4f7a33"/></linearGradient>
      <linearGradient id="footPaper" x1="0" y1="0" x2="0" y2="1"><stop offset="0" stop-color="#ffffff"/><stop offset="1" stop-color="#cfcfcf"/></linearGradient>
    </defs>
    <rect width="548" height="778" fill="url(#paperFront)"/>
    <path d="M0,100 C180,104 380,92 548,52 L548,400 L0,400 Z" fill="url(#lawnFront)" role="img" aria-label="Photo of a striped green lawn with a curving paved garden path"/>
    <path d="M140,102 C320,100 450,82 548,46 L548,64 C450,98 320,110 140,104 Z" fill="var(--purple)"/>
    <path d="M0,398 Q274,356 548,396 L548,778 L0,778 Z" fill="var(--purple)"/>
    <path d="M0,408 Q274,368 548,408 L548,778 L0,778 Z" fill="var(--green)"/>
    <path d="M0,714 Q274,680 548,712 L548,778 L0,778 Z" fill="var(--purple)"/>
    <path d="M0,724 Q274,692 548,722 L548,778 L0,778 Z" fill="url(#footPaper)"/>
    <g stroke="var(--purple)" stroke-width="4" fill="url(#thumb)">
      <circle cx="89" cy="362" r="51" role="img" aria-label="Photo of a gardener aerating a lawn"/>
      <circle cx="211" cy="340" r="51" role="img" aria-label="Photo of a spreader applying lawn treatment"/>
      <circle cx="333" cy="340" r="51" role="img" aria-label="Photo of turf being rolled out"/>
      <circle cx="454" cy="362" r="51" role="img" aria-label="Photo of a scarifier removing moss"/>
    </g>
    <path d="M110,697 l-14,6 l14,4 Z M426,697 l14,6 l-14,4 Z" fill="var(--green-deep)"/>
  </svg>

  <div class="brand"><span class="brand__dot"></span><span class="brand__name">Pelham Gardening Services</span></div>
  <h1 class="title">Expert Lawn<br>Treatment Service</h1>

  <h2 class="pill" style="top:418px">Treatments available:</h2>
  <ul class="checklist" style="top:442px;left:50px;right:50px">
    <li>Lawn Fertilising</li><li>Scarification</li><li>Aeration</li><li>Weed Control</li>
    <li>Moss Control</li><li>Hydration Booster</li><li>Kempix</li><li>Turfing &amp; Renovation</li>
  </ul>

  <div class="divider"></div>

  <h2 class="pill" style="top:544px">Services provided :</h2>
  <ul class="checklist" style="top:566px;font-size:13px">
    <li>Lawn mowing</li><li>Shrub pruning</li><li>Hedge trimming</li><li>Weed killing</li>
    <li>Garden clearance &amp; tidy-up</li><li>Planting &amp; design</li><li>Turfing</li>
    <li>Fencing</li><li>Gutter clearance</li>
  </ul>

  <p class="strap">Lawn Care by your Local Gardening Expert</p>
  <p class="invite">Select a one-off treatment or choose from one of our<br>Specially created lawn care packages.</p>
  <p class="contact">
    <svg class="contact__icon" viewBox="0 0 16 16"><circle cx="8" cy="8" r="7" fill="none" stroke="var(--green)" stroke-width="1.5"/><path d="M5.5 4.5l1.5 0 .7 2-1 .8a5 5 0 0 0 2 2l.8-1 2 .7v1.5c-3.5.5-6.5-2.5-6-6z" fill="var(--green)"/></svg>
    <span class="contact__phone">01632 960481</span> | www.pelhamgardening.co.uk/lawncare
  </p>
</section>

<!-- BACK SIDE -->
<section class="flyer flyer--back">
  <svg class="flyer__shapes" viewBox="0 0 548 778">
    <defs>
      <linearGradient id="paperBack" x1="0" y1="0" x2="0" y2="1"><stop offset="0" stop-color="#ffffff"/><stop offset="1" stop-color="#d6d6d6"/></linearGradient>
      <linearGradient id="lawnBack" x1="0" y1="0" x2="1" y2="1"><stop offset="0" stop-color="#8a8272"/><stop offset=".4" stop-color="#57a431"/><stop offset="1" stop-color="#6b8a4a"/></linearGradient>
      <linearGradient id="footPaperB" x1="0" y1="0" x2="0" y2="1"><stop offset="0" stop-color="#ffffff"/><stop offset="1" stop-color="#cfcfcf"/></linearGradient>
    </defs>
    <rect width="548" height="778" fill="url(#paperBack)"/>
    <path d="M0,100 C180,104 380,92 548,52 L548,400 L0,400 Z" fill="url(#lawnBack)" role="img" aria-label="Photo of a freshly striped lawn bordered by a block-paved path and flower beds"/>
    <path d="M140,102 C320,100 450,82 548,46 L548,64 C450,98 320,110 140,104 Z" fill="var(--purple)"/>
    <path d="M0,392 Q300,355 548,364 L548,778 L0,778 Z" fill="var(--purple)"/>
    <path d="M0,404 Q300,368 548,376 L548,778 L0,778 Z" fill="var(--green)"/>
    <path d="M0,714 Q274,680 548,712 L548,778 L0,778 Z" fill="var(--purple)"/>
    <path d="M0,724 Q274,692 548,722 L548,778 L0,778 Z" fill="url(#footPaperB)"/>
  </svg>

  <div class="brand"><span class="brand__dot"></span><span class="brand__name">Pelham Gardening Services</span></div>
  <h1 class="title">Expert Lawn<br>Treatment Service</h1>

  <p class="copy copy--intro">As expert gardeners, we are passionate about horticulture and working to bring out the very best in your garden. When we work in your garden, we look at it and treat it with the same care and attention as if it were our own, before handing it back for you to enjoy. Our passion doesn't end at just trees and shrubs though. Your grass is as much of a living, breathing plant as your shrubs and we therefore utilise our expert horticultural knowledge to ensure your lawn thrives and reaches its fullest potential.</p>

  <div class="packages">
    <h2 class="packages__title">Lawn Treatment Packages</h2>
    <table>
      <thead><tr><th></th><th>STANDARD PACKAGE</th><th>ENHANCED PACKAGE</th><th>PREMIUM PACKAGE</th></tr></thead>
      <tbody>
        <tr><td>Spring Treatment</td><td><i class="tick"></i></td><td><i class="tick"></i></td><td><i class="tick"></i></td></tr>
        <tr><td>Early Summer Treatment</td><td><i class="tick"></i></td><td><i class="tick"></i></td><td><i class="tick"></i></td></tr>
        <tr><td>Late Summer Treatment</td><td><i class="tick"></i></td><td><i class="tick"></i></td><td><i class="tick"></i></td></tr>
        <tr><td>Autumn/Winter Treatment</td><td><i class="tick"></i></td><td><i class="tick"></i></td><td><i class="tick"></i></td></tr>
        <tr><td>Scarification</td><td></td><td><i class="tick"></i></td><td><i class="tick"></i></td></tr>
        <tr><td>Aeration</td><td></td><td><i class="tick"></i></td><td><i class="tick"></i></td></tr>
        <tr><td>Kempix Treatment</td><td></td><td></td><td><i class="tick"></i></td></tr>
        <tr><td>Hydration Boost Treatment</td><td></td><td></td><td><i class="tick"></i></td></tr>
      </tbody>
    </table>
  </div>

  <p class="copy copy--detail">Lawn care isn't just about applying a fertiliser. It's about really understanding your lawn and being able to use extensive knowledge and experience to diagnose and treat issues. It therefore stands to reason that you should employ an expert to bring out the best in your lawn which is why we at Pelham Gardening Services have created a superior lawn care service that will keep your lawn looking lush, green and healthy all year round.</p>

  <p class="invite">Select a one-off treatment or choose from one of our<br>Specially created lawn care packages.</p>
  <p class="contact">
    <svg class="contact__icon" viewBox="0 0 16 16"><circle cx="8" cy="8" r="7" fill="none" stroke="var(--green)" stroke-width="1.5"/><path d="M5.5 4.5l1.5 0 .7 2-1 .8a5 5 0 0 0 2 2l.8-1 2 .7v1.5c-3.5.5-6.5-2.5-6-6z" fill="var(--green)"/></svg>
    <span class="contact__phone">01632 960481</span> | www.pelhamgardening.co.uk/lawncare
  </p>
</section>

</body>
</html>
```